依頼詳細
【サイトの最大の要望】
・ターゲットに合った分かりやすいデザイン

【強み】
・整体と美容の両方からお客様の身体の不調やなりたい自分に合った施術を行える点です。

【おすすめメニュー】
・お客様の身体の不調や気になる部分に合わせたオーダーメイドの施術

【ターゲット】
・30代・40代の会社員、自営、パートなど自分にかけるお金がある人。

【デザインについて】
・部分的に参考サイトのようなフレームを使用していただきたいです。
・参考サイトの「お知らせ」の背景で使用しているような
お花などのボタニカルなイラストなど入れてほしいです。

【参考サイト】
・tonsor HALVEN MOREL(トンソル ハルヴェン モレル)
http://morel-tonsor.example/
白を基調としている点や、上品なゴールドのフォント、「お知らせ」の背景で使用している
お花のイラストをアクセントで使用しているところが気に入っています。

http://quillmere-works.example/
とても見やすくて分かりやすくていいなと思っています。

http://vesna-lumio.example/
フレームや両隅の装飾が好きです。

http://kp-dermaluxe.example/
色合いやテクスチャー、お花のイラストなどが女性らしい雰囲気でイメージに一番近いです。

【サイトマップ】
①TOP
② アクセス
③初めての方へ
④プロフィール
⑤ 当サロンの特徴
⑥身体の外側の不調(痛み・しびれ)
⑦身体の内側の不調(内臓などの不調・冷え症・アトピー)
⑧ストレス
⑨顔に関するお悩み
⑩体に関するお悩み
⑪リラクゼーション
⑫お客様の声
⑬キャンペーン、特典
⑭セミナー・スクールのご案内
⑮料金
⑯ニュース(一覧)
∟⑰ニュース(詳細)
⑱ブログ(一覧)
∟⑲ブログ(詳細)
⑳予約、お問い合わせ、プライバシー・ポリシー

■TOPページにGメニューとは別にデザインの入り口を必須で設けて頂きたいコンテンツは以下となります。
(それ以外のページに関してはランサーにお任せします)

タイトル:メニュー
⑥身体の外側の不調(痛み・しびれ)
⑧ストレス
⑨顔に関するお悩み
⑩体に関するお悩み
⑪リラクゼーション

⑫お客様の声
⑬キャンペーン、特典
⑰ニュース(詳細)
⑲ブログ(詳細)

下記のボタンもしくはバナー希望です。
・予約
・お問い合わせ
・キャンペーン
サイトURL
https://trelvane.sitebloomer.example/
ページ数
1ページ
希望イメージ
シンプル 複雑
単色 カラフル
暗い 明るい
日常 高級
遊び心 厳粛
未来的 伝統的
女性的 男性的
希望する色
緑系、ゴールド
納品ファイル
• イラストレーター形式 (.ai)
• フォトショップ形式 (.psd)
• PNG形式 (.png)
補足説明
【店舗へのご連絡はおやめください】
ワークリンク規約にもありますが、店舗への通常業務に支障が出るため、
直接電話等のお問い合わせをお控え頂きますよう、ご協力願います。

【素材写真】
下記よりダウンロードしてご使用ください。
https://3.filedrift.example/0225-k81937b52c904f6a13bd7e2059c771b3
TOPイメージを添付しましたので、延長を希望いたします。

下記よりダウンロードしてご参照ください。
https://20.filedrift.example/0131-p47390a81be527c09d6f1a38e4b92c05

ご多忙のところ恐縮ですが、宜しくお願いいたします。
テキストや画像などのダミーは無い状態でご提案をお願いいたします。

全体的にバランスが良く、整体っぽくないメインビジュアルが特に良かったです。

たくさんのご提案、ありがとうございました。
どのデザインも素敵で選定が難しかったです。

また、何か機会がありましたら、宜しくお願いいたします。

```html
<!DOCTYPE html>
<html lang="ja">
<head>
<meta charset="utf-8">
<title>Trelvane | 整体・美容サロン</title>
<link href="https://fonts.googleapis.com/css2?family=Cormorant+Garamond:ital,wght@0,500;1,500;1,600&family=Noto+Serif+JP:wght@400;500;600&display=swap" rel="stylesheet">
<style>
:root{
  --gold:#c6a43a;
  --gold-light:#e0c768;
  --gold-deep:#a9862a;
  --ink:#4a4a4a;
  --muted:#8a8a8a;
  --mint:#d8eeed;
  --mint-soft:#eef7f6;
  --grey-bg:#f2f2f2;
  --line:#d9d9d9;
  --white:#ffffff;
}
*{box-sizing:border-box;margin:0;padding:0}
html,body{width:1200px;height:5400px;overflow:hidden}
body{position:relative;background:var(--white);color:var(--ink);font-family:"Noto Serif JP",serif;font-size:16px;line-height:1.8}
.en{font-family:"Cormorant Garamond",serif;font-style:italic;color:var(--gold)}
.abs{position:absolute}

/* header / hero */
.hero{left:0;top:0;width:1200px;height:720px;background:linear-gradient(120deg,#eef1f2 0%,#e2e6e8 45%,#f4f5f6 100%)}
.gnav{right:30px;top:18px;display:flex;gap:26px;z-index:2}
.gnav a{text-decoration:none;text-align:center;display:block}
.gnav .en{font-size:17px;display:block;line-height:1.2}
.gnav small{font-size:10px;color:var(--muted)}
.brand{left:0;width:1200px;top:210px;text-align:center;font-family:"Cormorant Garamond",serif;font-style:italic;font-weight:600;font-size:76px;color:var(--gold)}
.side-btns{right:0;top:238px;width:240px;display:flex;flex-direction:column;gap:8px}
.side-btns a{display:block;height:56px;line-height:56px;padding-left:26px;text-decoration:none;background:linear-gradient(90deg,var(--gold-deep),var(--gold-light));color:var(--white);font-family:"Cormorant Garamond",serif;font-style:italic;font-size:24px}

/* information */
.info-box{left:0;top:690px;width:240px;height:180px;background:linear-gradient(135deg,var(--gold-light),var(--gold-deep));text-align:center;padding-top:46px}
.info-box h2{font-family:"Cormorant Garamond",serif;font-style:italic;font-weight:500;color:var(--white);font-size:30px}
.info-box a{display:inline-block;margin-top:16px;border:1px solid var(--white);color:var(--white);font-size:11px;padding:2px 30px;text-decoration:none}
.news-row{left:290px;top:760px;width:860px;border-bottom:1px solid var(--line);padding-bottom:12px;font-size:15px}
.news-row time{margin-right:46px;color:var(--muted)}

/* concept */
.flora{border-radius:50%;filter:blur(2px)}
.concept{left:0;top:990px;width:1200px;text-align:center}
.sec-title{font-family:"Cormorant Garamond",serif;font-style:italic;font-weight:500;color:var(--gold);font-size:40px;line-height:1}
.concept h3{font-size:26px;font-weight:500;margin:22px 0 24px;letter-spacing:.12em}
.concept p{font-size:15px;line-height:2}

/* campaign */
.campaign-band{left:0;top:1500px;width:1200px;height:400px;background:var(--grey-bg)}
.campaign-card{left:240px;top:1620px;width:720px;height:180px;background:var(--white);display:flex}
.campaign-card .text{flex:1;padding:14px 26px}
.campaign-card .en{font-size:28px}
.campaign-card h4{font-size:20px;font-weight:500;margin-top:6px}
.campaign-card .red{color:#d7574b;font-size:12px;line-height:1.5}
.campaign-card .gold{color:var(--gold-deep);font-size:15px}
.campaign-card .price{font-size:12px}
.campaign-card .photo{width:360px;background:linear-gradient(135deg,#e9d3c4,#c7a08c)}

/* menu */
.ornament{height:70px;width:300px;left:450px;top:2080px;background:radial-gradient(ellipse at center,#efe2b2 0%,rgba(239,226,178,0) 70%)}
.menu-title{left:0;width:1200px;top:2170px;text-align:center}
.menu-grid{left:220px;top:2270px;width:760px;display:grid;grid-template-columns:repeat(3,240px);column-gap:20px;row-gap:50px}
.menu-card{height:200px;position:relative}
.menu-card .photo{height:160px;display:flex;flex-direction:column;align-items:center;justify-content:center;color:var(--white)}
.menu-card .photo strong{font-weight:500;font-size:18px}
.menu-card .photo span{font-size:10px}
.menu-card .photo em{font-family:"Cormorant Garamond",serif;font-size:22px}
.menu-card .bar{height:30px;background:var(--mint);font-size:11px;color:var(--muted);display:flex;align-items:center;justify-content:center;gap:30px}
.menu-card .bar b{font-family:"Cormorant Garamond",serif;font-style:italic;font-weight:500;color:var(--gold)}

/* voice */
.voice-bg{left:0;top:2880px;width:1200px;height:740px;background:linear-gradient(180deg,var(--white) 0%,var(--mint-soft) 100%)}
.voice-title{left:0;width:1200px;top:2950px;text-align:center}
.voice-title small{display:block;font-size:12px;color:var(--muted);margin-top:6px}
.voices{left:210px;top:3030px;width:780px;display:flex;gap:36px}
.voice-card{width:236px;height:290px;background:var(--white);border:1px solid #bdbdbd;padding:10px}
.voice-card .head{font-size:10px;border-bottom:1px solid #bdbdbd;margin-bottom:6px}
.voice-card .sheet{height:240px;background:repeating-linear-gradient(180deg,#fff 0 22px,#e6e6e6 22px 23px)}

/* seminar & blog */
.sb-band{left:0;top:3700px;width:1200px;height:460px}
.panel{top:3720px;width:460px;height:430px;background:var(--mint);text-align:center;padding-top:26px}
.panel .sec-title{font-size:34px}
.seminar{left:120px}
.seminar .photo{margin:22px auto 0;width:360px;height:110px;background:linear-gradient(135deg,#d9c1b3,#9f7f70)}
.seminar h4{font-size:14px;font-weight:500;margin-top:12px}
.seminar p{width:360px;margin:6px auto 0;text-align:left;font-size:11px;line-height:1.7}
.seminar a{display:inline-block;margin-top:12px;background:var(--white);color:var(--muted);border:1px solid var(--line);font-size:12px;padding:4px 46px;text-decoration:none}
.blog{left:680px}
.blog ul{list-style:none;margin:26px 60px 0;text-align:left}
.blog li{display:flex;gap:20px;margin-bottom:30px}
.blog li .photo{width:160px;height:110px;background:linear-gradient(135deg,#e6d2c4,#b89583)}
.blog li time{display:block;font-size:13px}
.blog li span{font-size:13px}

/* map */
.map-title{left:0;width:1200px;top:4175px;text-align:center}
.map{left:0;top:4230px;width:1200px;height:800px;background:linear-gradient(135deg,#eef0ec,#e3e6e1)}

/* footer */
.shop{left:0;top:5000px;width:600px;height:400px;background:var(--mint);padding:50px 0 0 24px}
.shop h5{font-size:17px;font-weight:500;border-bottom:1px solid var(--ink);width:180px;padding-bottom:10px}
.shop .en{display:block;margin-top:18px;font-size:24px;color:var(--ink)}
.shop .tel{font-size:44px;line-height:1.1;font-family:"Cormorant Garamond",serif;font-weight:500}
.shop .tel svg{vertical-align:middle}
.shop address{font-style:normal;font-size:15px;line-height:1.6}
.storefront{left:600px;top:5000px;width:600px;height:400px;background:linear-gradient(180deg,#5c7f93 0%,#8fa6ae 55%,#c2b9a4 100%)}
</style>
</head>
<body>

<!-- hero -->
<div class="abs hero" role="img" aria-label="顔のマッサージを受けてリラックスする女性の写真"></div>
<nav class="abs gnav">
  <a href="#"><span class="en">Top</span><small>トップ</small></a>
  <a href="#"><span class="en">Salon</span><small>サロン</small></a>
  <a href="#"><span class="en">Beginner</span><small>初めての方へ</small></a>
  <a href="#"><span class="en">Profile</span><small>プロフィール</small></a>
  <a href="#"><span class="en">Menu</span><small>メニュー</small></a>
  <a href="#"><span class="en">Voice</span><small>お客様の声</small></a>
  <a href="#"><span class="en">Price</span><small>料金</small></a>
  <a href="#"><span class="en">Campaign</span><small>特典</small></a>
  <a href="#"><span class="en">Seminar&amp;School</span><small>セミナー・スクール</small></a>
  <a href="#"><span class="en">Access</span><small>アクセス</small></a>
</nav>
<h1 class="abs brand">Trelvane</h1>
<div class="abs side-btns">
  <a href="#">Reservation</a>
  <a href="#">Contact</a>
  <a href="#">Campaign</a>
</div>

<!-- information -->
<section class="abs info-box">
  <h2>Information</h2>
  <a href="#">MORE</a>
</section>
<p class="abs news-row"><time>2020.1.15</time>ホームページリニューアルのお知らせ</p>

<!-- concept -->
<div class="abs flora" style="left:0;top:880px;width:420px;height:110px;background:radial-gradient(ellipse at 40% 50%,#b9d9e6 0%,#d9e8ef 45%,rgba(255,255,255,0) 72%)" role="img" aria-label="水彩の花のイラスト"></div>
<div class="abs flora" style="left:930px;top:1100px;width:270px;height:250px;background:radial-gradient(ellipse at 60% 50%,#bfdde4 0%,#dcecef 45%,rgba(255,255,255,0) 72%)" role="img" aria-label="水彩の花と葉のイラスト"></div>
<section class="abs concept">
  <h2 class="sec-title">Concept</h2>
  <h3>身体のなかを整え、キレイと健康を手に入れる</h3>
  <p>人には5つの流れがあります。<br>
  それは「血液」「リンパ」「神経」「脳脊髄液」「筋膜」。<br>
  この5つの流れを改善し整えることで、<br>
  身体がもともと持っている力を取り戻し、本当の健康を保つことができるのです。<br>
  Trelvaneでは整体と美容の両面から、お一人おひとりの不調となりたい自分に寄り添い、<br>
  身体の内側と外側の両方を丁寧に整える、オーダーメイドの施術をご提供いたします。</p>
</section>

<!-- campaign -->
<div class="abs campaign-band"></div>
<article class="abs campaign-card">
  <div class="text">
    <span class="en">Campaign</span>
    <h4>春の美肌キャンペーン</h4>
    <p class="red">フェイシャルと小顔矯正をセットにした春だけの特別プラン<br>初めての方も安心してお試しいただけます</p>
    <p class="gold">整体＋フェイシャル＋小顔ケア</p>
    <p class="price">通常 ¥16,000(税込) → ¥13,800(税込)</p>
  </div>
  <div class="photo" role="img" aria-label="背中の施術を受ける女性の写真"></div>
</article>

<!-- menu -->
<div class="abs ornament" role="img" aria-label="金色の装飾フレーム"></div>
<h2 class="abs sec-title menu-title">Menu</h2>
<div class="abs menu-grid">
  <div class="menu-card"><div class="photo" style="background:linear-gradient(135deg,#b7a79c,#7d6b63)" role="img" aria-label="肩の施術の写真"><strong>身体の外側の不調</strong><span>痛み・しびれ</span></div><div class="bar"><b>Health</b>外側</div></div>
  <div class="menu-card"><div class="photo" style="background:linear-gradient(135deg,#c9b9ab,#8e7a6e)" role="img" aria-label="腹部の施術の写真"><strong>身体の内側の不調</strong><span>冷え症・内臓の不調</span></div><div class="bar"><b>Health</b>内側</div></div>
  <div class="menu-card"><div class="photo" style="background:linear-gradient(135deg,#a89890,#6f5f59)" role="img" aria-label="頭の施術の写真"><strong>ストレス</strong></div><div class="bar"><b>Health</b>ストレス</div></div>
  <div class="menu-card"><div class="photo" style="background:linear-gradient(135deg,#e3d2c6,#b49c8e)" role="img" aria-label="フェイシャルケアの写真"><em>Face</em><span>顔のお悩み</span></div><div class="bar"><b>Beauty</b>顔</div></div>
  <div class="menu-card"><div class="photo" style="background:linear-gradient(135deg,#d8c3b4,#9b8274)" role="img" aria-label="ボディケアの写真"><em>Body</em><span>体のお悩み</span></div><div class="bar"><b>Beauty</b>体</div></div>
  <div class="menu-card"><div class="photo" style="background:linear-gradient(135deg,#cdb6a8,#8f7365)" role="img" aria-label="リラクゼーションの写真"><em>Relaxation</em><span>リラクゼーション</span></div><div class="bar"><b>Relax</b>癒し</div></div>
</div>

<!-- voice -->
<div class="abs voice-bg"></div>
<div class="abs flora" style="left:0;top:2790px;width:380px;height:300px;background:radial-gradient(ellipse at 45% 45%,#e7a7b6 0%,#b5d3e0 40%,rgba(255,255,255,0) 72%)" role="img" aria-label="ピンクと青の花のイラスト"></div>
<div class="abs flora" style="left:880px;top:3500px;width:320px;height:300px;background:radial-gradient(ellipse at 55% 50%,#f0a89a 0%,#f4cdb9 40%,rgba(255,255,255,0) 72%)" role="img" aria-label="オレンジの花のイラスト"></div>
<h2 class="abs sec-title voice-title">Voice<small>お客様の声</small></h2>
<div class="abs voices">
  <div class="voice-card"><p class="head">ご感想アンケート</p><div class="sheet" role="img" aria-label="手書きのお客様アンケート"></div></div>
  <div class="voice-card"><p class="head">ご感想アンケート</p><div class="sheet" role="img" aria-label="手書きのお客様アンケート"></div></div>
  <div class="voice-card"><p class="head">ご感想アンケート</p><div class="sheet" role="img" aria-label="手書きのお客様アンケート"></div></div>
</div>

<!-- seminar & blog -->
<section class="abs panel seminar">
  <h2 class="sec-title">Seminar &amp; School</h2>
  <div class="photo" role="img" aria-label="セミナーで施術を学ぶ様子の写真"></div>
  <h4>若葉ボディメイクスクールのご案内</h4>
  <p>Trelvaneでは、整体と美容の技術を学べるセミナーとスクールを開講しています。基礎から丁寧にお伝えし、現場ですぐに活かせる手技を身につけていただけます。初心者の方もお気軽にご相談ください。</p>
  <a href="#">詳しく見る</a>
</section>
<section class="abs panel blog">
  <h2 class="sec-title">Blog</h2>
  <ul>
    <li><div class="photo" role="img" aria-label="施術中の写真"></div><div><time>2019.12.1</time><span>シンクラー整体</span></div></li>
    <li><div class="photo" role="img" aria-label="腹部の施術の写真"></div><div><time>2020.1.12</time><span>内臓調整施術</span></div></li>
  </ul>
</section>

<!-- map -->
<h2 class="abs sec-title map-title">Map</h2>
<div class="abs map" role="img" aria-label="サロン周辺の地図"></div>

<!-- footer -->
<section class="abs shop">
  <h5>店舗情報</h5>
  <span class="en">Tel</span>
  <p class="tel"><svg width="30" height="30" viewBox="0 0 24 24"><path d="M6.6 10.8a15 15 0 0 0 6.6 6.6l2.2-2.2a1 1 0 0 1 1-.25 11.4 11.4 0 0 0 3.6.57 1 1 0 0 1 1 1V20a1 1 0 0 1-1 1A17 17 0 0 1 3 4a1 1 0 0 1 1-1h3.5a1 1 0 0 1 1 1c0 1.25.2 2.45.57 3.57a1 1 0 0 1-.25 1z" fill="#4a4a4a"/></svg> 090-4826-3017</p>
  <span class="en">Address</span>
  <address>神奈川県横浜市緑区若葉台2-7-9<br>ハルネ若葉ビル203</address>
</section>
<div class="abs storefront" role="img" aria-label="夕暮れのサロン入口の写真"></div>

</body>
</html>
```